Community Wellness FAIR 2023 Presenters

We need an image design that shows all of the presenters in our upcoming professional workshop. We will use this to promote in email newsletters, social media posts, and on our program website. The image should include the presenter's photo, full name with letters after their names, the FAIR logo, and the full program title. The details are listed below:

FAIR 2023 design Instructions

Program title:
Community Wellness Advisory & Venture FAIR 2023

Presenters Names:

Miranda Pollock Fairbairn, PhD, MPH - (should be positioned as the highlight, the leader, or main attraction)

Ronald Sutcliffe-Moor, MPH
Bethany Quarrington, MPH
Lorette Pemberly, PhD, MS, MPH
Greta Lindqvar, MPH
Tamira' Dobbs, MPH
Wallace Brisk, MPH
Dariel Fontaine, MS, MPH
Marisol Ochoa, MPH
Poppy Mercer, MS
Keisha Lomond, BS
Pavitra Ramalingaswamy, MPH
Talisha Cromby, DrPH, MS
Greta Vollmarin, MPH
Rosalind Tabbert, MPH

Brand colors:
#56588C
#F2E088
#F28444
#F24C27
#0D0D0D

```html
<!DOCTYPE html>
<html lang="en">
<head>
<meta charset="utf-8">
<title>Community Wellness FAIR 2023 Presenters</title>
<link href="https://fonts.googleapis.com/css2?family=Montserrat:wght@500;600;700&family=Playfair+Display:wght@700&display=swap" rel="stylesheet">
<style>
  :root {
    --purple: #56588C;
    --yellow: #F2E088;
    --yellow-soft: #F4E59A;
    --orange: #F28444;
    --red: #F24C27;
    --ink: #0D0D0D;
    --white: #FFFFFF;
  }
  * { box-sizing: border-box; margin: 0; padding: 0; }
  html, body { width: 720px; height: 1200px; overflow: hidden; }
  body { background: var(--white); font-family: "Montserrat", sans-serif; }
  .poster {
    position: relative; width: 720px; height: 1200px;
    background: var(--yellow-soft); overflow: hidden;
  }
  .brand {
    position: absolute; top: 26px; left: 0; width: 720px;
    display: flex; justify-content: center; align-items: center; gap: 10px;
  }
  .brand-dot { width: 22px; height: 22px; border-radius: 50%; background: var(--red); }
  .brand-name {
    font-weight: 700; font-size: 24px; color: var(--orange); letter-spacing: 0.5px;
  }
  .rule {
    position: absolute; left: 28px; width: 664px; height: 20px; background: var(--purple);
  }
  .rule.top { top: 88px; }
  .rule.mid { top: 442px; }
  .hero {
    position: absolute; top: 120px; left: 28px; width: 664px; height: 312px;
    background: linear-gradient(120deg, #F6F8FA 0%, #DCE7EF 45%, #9FB8CC 75%, #5E7891 100%);
  }
  .welcome {
    position: absolute; top: 150px; left: 96px; width: 528px; height: 236px;
    background: rgba(255,255,255,0.72);
    display: flex; flex-direction: column; justify-content: center; align-items: center;
    text-align: center; padding: 0 30px; color: var(--purple);
  }
  .welcome-kicker {
    font-family: "Playfair Display", serif; font-size: 22px; letter-spacing: 2px; margin-bottom: 12px;
  }
  .welcome-title {
    font-family: "Playfair Display", serif; font-weight: 700; font-size: 32px;
    line-height: 1.2; text-transform: uppercase;
  }
  .presenters {
    position: absolute; top: 488px; left: 28px; width: 664px;
    display: grid; grid-template-columns: repeat(5, 120px); column-gap: 16px; row-gap: 22px;
  }
  .presenter { text-align: center; }
  .portrait { width: 120px; height: 128px; }
  .tone-a { background: #C9B7A6; }
  .tone-b { background: #A98E7C; }
  .tone-c { background: #7E6A60; }
  .tone-d { background: #D7C7B8; }
  .tone-e { background: #8C8F96; }
  .presenter-name {
    margin-top: 6px; font-size: 9px; font-weight: 600; text-transform: uppercase;
    letter-spacing: 0.6px; color: var(--ink); line-height: 1.2;
  }
  .presenter-creds { font-size: 8px; font-weight: 500; color: var(--ink); margin-top: 2px; }
  .presenter.lead .presenter-name, .presenter.lead .presenter-creds { color: var(--orange); font-weight: 700; }
  .footer-band {
    position: absolute; top: 1088px; left: 28px; width: 664px; height: 48px;
    background: var(--purple); display: flex; justify-content: center; align-items: center;
  }
  .site { font-size: 20px; font-weight: 600; color: var(--yellow); letter-spacing: 0.5px; }
</style>
</head>
<body>
<main class="poster">
  <header class="brand">
    <span class="brand-dot"></span>
    <span class="brand-name">Community Wellness FAIR</span>
  </header>

  <div class="rule top"></div>
  <div class="hero" role="img" aria-label="Photograph of a laboratory microscope"></div>
  <section class="welcome">
    <p class="welcome-kicker">WELCOME TO</p>
    <h1 class="welcome-title">Community Wellness Advisory &amp; Venture FAIR 2023</h1>
  </section>
  <div class="rule mid"></div>

  <section class="presenters">
    <article class="presenter"><div class="portrait tone-d" role="img" aria-label="Portrait of Ronald Sutcliffe-Moor"></div><p class="presenter-name">Ronald Sutcliffe-Moor</p><p class="presenter-creds">MPH</p></article>
    <article class="presenter"><div class="portrait tone-c" role="img" aria-label="Portrait of Bethany Quarrington"></div><p class="presenter-name">Bethany Quarrington</p><p class="presenter-creds">MPH</p></article>
    <article class="presenter"><div class="portrait tone-a" role="img" aria-label="Portrait of Lorette Pemberly"></div><p class="presenter-name">Lorette Pemberly</p><p class="presenter-creds">PhD, MS, MPH</p></article>
    <article class="presenter"><div class="portrait tone-d" role="img" aria-label="Portrait of Greta Lindqvar"></div><p class="presenter-name">Greta Lindqvar</p><p class="presenter-creds">MPH</p></article>
    <article class="presenter"><div class="portrait tone-b" role="img" aria-label="Portrait of Tamira' Dobbs"></div><p class="presenter-name">Tamira' Dobbs</p><p class="presenter-creds">MPH</p></article>

    <article class="presenter"><div class="portrait tone-e" role="img" aria-label="Portrait of Wallace Brisk"></div><p class="presenter-name">Wallace Brisk</p><p class="presenter-creds">MPH</p></article>
    <article class="presenter"><div class="portrait tone-c" role="img" aria-label="Portrait of Dariel Fontaine"></div><p class="presenter-name">Dariel Fontaine</p><p class="presenter-creds">MS, MPH</p></article>
    <article class="presenter lead"><div class="portrait tone-b" role="img" aria-label="Portrait of Miranda Pollock Fairbairn"></div><p class="presenter-name">Miranda Pollock Fairbairn</p><p class="presenter-creds">PhD, MPH</p></article>
    <article class="presenter"><div class="portrait tone-d" role="img" aria-label="Portrait of Marisol Ochoa"></div><p class="presenter-name">Marisol Ochoa</p><p class="presenter-creds">MPH</p></article>
    <article class="presenter"><div class="portrait tone-a" role="img" aria-label="Portrait of Poppy Mercer"></div><p class="presenter-name">Poppy Mercer</p><p class="presenter-creds">MS</p></article>

    <article class="presenter"><div class="portrait tone-c" role="img" aria-label="Portrait of Keisha Lomond"></div><p class="presenter-name">Keisha Lomond</p><p class="presenter-creds">BS</p></article>
    <article class="presenter"><div class="portrait tone-a" role="img" aria-label="Portrait of Pavitra Ramalingaswamy"></div><p class="presenter-name">Pavitra Ramalingaswamy</p><p class="presenter-creds">MPH</p></article>
    <article class="presenter"><div class="portrait tone-e" role="img" aria-label="Portrait of Talisha Cromby"></div><p class="presenter-name">Talisha Cromby</p><p class="presenter-creds">DrPH, MS</p></article>
    <article class="presenter"><div class="portrait tone-d" role="img" aria-label="Portrait of Greta Vollmarin"></div><p class="presenter-name">Greta Vollmarin</p><p class="presenter-creds">MPH</p></article>
    <article class="presenter"><div class="portrait tone-b" role="img" aria-label="Portrait of Rosalind Tabbert"></div><p class="presenter-name">Rosalind Tabbert</p><p class="presenter-creds">MPH</p></article>
  </section>

  <footer class="footer-band">
    <p class="site">wellnessfairhub.com</p>
  </footer>
</main>
</body>
</html>
```